Webdesign for Non profit Diabetes education company

We are looking for a website design for our company.

We just created the company Glucose Guidance Circle

The concept for the company is to educate diabetics with resources that will help them manage their Diabetes. The list of advisers will be dietitians, podiatrist, diabetic educators, and fitness centers.

Please see attached logo. I like the logo to include an image that connects people together.

I've attached our logo, please use the colors in the design of the site.

Creativity is encouraged. Have fun with this project. We are looking for a professional site but not to corporate.

The page must be written in HTML 5 and be responsive built for mobile. You can use bootstrap, jquery, or angular JS.

Wordpress or wix will not be accepted.

The website will be hosted at www.glucoseguidancecircle.com

Industry/Entity Type

Education

Coding

Coded - Design and coding required

Number of Pages Required

3 page

Requirements
Must have
• The page must be written in HTML 5 and be responsive built for mobile. You can use bootstrap, jquery, or angular JS.
• The landing page should include a splash page. Please incorporate the logo and the
Should not have
• Wordpress or wix will not be accepted.

```html
<!DOCTYPE html>
<html lang="en">
<head>
<meta charset="utf-8">
<title>Glucose Guidance Circle</title>
<link href="https://fonts.googleapis.com/css2?family=Roboto:wght@400;500;700&display=swap" rel="stylesheet">
<style>
:root{
  --pink:#f45e8a;
  --blue:#6b8fcf;
  --ink:#222;
  --muted:#555;
  --panel:#ebebeb;
  --tab:#8a8a8a;
  --hero-a:#f6f6f6;
  --hero-b:#e6e6e6;
}
*{margin:0;padding:0;box-sizing:border-box}
html,body{width:1200px;height:1200px;overflow:hidden;background:#fff}
body{position:relative;font-family:"Roboto",Arial,sans-serif;color:var(--ink)}
.abs{position:absolute}
.social{top:13px;left:554px;display:flex;gap:8px}
.social span{width:16px;height:16px;border:1.3px solid #333;border-radius:50%;display:block}
.header{left:346px;top:40px;width:506px;height:42px;background:#f3f3f3;border-bottom:2px solid var(--pink)}
.brand{position:absolute;left:13px;top:10px;display:flex;align-items:center;gap:5px;color:var(--pink);font-weight:500;font-size:12px;letter-spacing:.5px}
.brand i{width:20px;height:20px;border:2px solid var(--blue);border-radius:50%;display:block}
.nav{position:absolute;right:0;top:0;height:40px;display:flex;font-size:10px;color:#333}
.nav a{display:flex;align-items:center;padding:0 12px;text-decoration:none;color:inherit}
.nav a.active{background:var(--pink);color:#fff;font-weight:500;padding:0 14px}
.hero{left:346px;top:82px;width:506px;height:232px;background:linear-gradient(180deg,var(--hero-a),var(--hero-b))}
.hero-art{position:absolute;left:38px;top:38px;width:300px;height:160px;border-radius:8px;background:radial-gradient(ellipse at 60% 50%,#e3d6d6,#efe9e9 70%)}
.hero-brand{position:absolute;left:344px;top:92px;display:flex;flex-direction:column;align-items:center;gap:6px;color:var(--pink);font-weight:500;font-size:17px;letter-spacing:.5px;text-align:center;line-height:1.1}
.hero-brand i{width:50px;height:50px;border:4px solid var(--blue);border-radius:50%;display:block}
.quote{left:346px;top:314px;width:506px;height:56px;background:var(--pink);color:#fff;font-weight:700;font-size:8.6px;line-height:10.5px;padding:13px 13px 0}
.h2{font-size:9.8px;font-weight:500;text-decoration:underline;line-height:12px;text-transform:uppercase;left:359px;width:490px}
.stat{width:150px}
.stat svg{display:block;margin-left:0}
.stat h3,.card h3{font-size:10px;font-weight:500;margin-top:4px}
.stat p,.card p{font-size:7px;line-height:8.7px;color:var(--muted)}
.panel{left:346px;top:588px;width:506px;height:360px;background:var(--panel)}
.card{width:125px}
.card .icon{width:56px;height:56px;border-radius:50%;background:#fff;position:relative;margin-bottom:7px}
.card .icon div{position:absolute;inset:12px;border-radius:50%;background:linear-gradient(135deg,var(--blue),var(--pink));opacity:.55}
.info{left:359px;width:480px;font-size:6.9px;line-height:8.8px;color:var(--muted)}
.info b{font-weight:500;color:#333}
.info p{margin-bottom:8px}
.footer{left:346px;top:1170px;width:508px;height:30px;background:#f0f0f0;font-size:7px;color:#333;display:flex;justify-content:space-between;align-items:center;padding:0 13px}
.tab{left:941px;width:29px;background:var(--tab);color:#fff;font-size:7.5px;display:flex;align-items:center;justify-content:center}
.tab span{transform:rotate(-90deg);white-space:nowrap}
</style>
</head>
<body>
<div class="abs social"><span></span><span></span><span></span><span></span></div>

<header class="abs header">
  <div class="brand"><i></i>Glucose Guidance Circle</div>
  <nav class="nav"><a class="active">Home</a><a>Find Healthcare Provider</a><a>Blog</a></nav>
</header>

<section class="abs hero">
  <div class="hero-art" role="img" aria-label="Illustration of an older couple linked to icons of a pedorthist, diabetic educator, endocrinologist, nutritionist and podiatrist"></div>
  <div class="hero-brand"><i></i>GLUCOSE GUIDANCE<br>CIRCLE</div>
</section>

<div class="abs quote">"AT THE GLUCOSE GUIDANCE CIRCLE, OUR FOCUS IS TO CONNECT NEWLY DIAGNOSED AND EXISTING PATIENTS WITH DIABETES TO A NETWORK OF AVAILABLE PROFESSIONALS WHO POSSESS THE KNOWLEDGE TO MANAGE YOUR DIABETES."</div>

<h2 class="abs h2" style="top:390px">Diabetes occurs when your blood glucose, also called blood sugar, is too high.<br>High blood glucose can cause health problems over time.</h2>

<div class="abs stat" style="left:359px;top:434px">
  <svg width="88" height="88" viewBox="0 0 88 88"><circle cx="44" cy="44" r="41" fill="none" stroke="var(--blue)" stroke-width="5"/><text x="44" y="47" text-anchor="middle" font-size="9" fill="#222" font-family="Roboto,Arial,sans-serif">30.3 MILLION</text></svg>
  <h3>Total</h3><p>An estimated 30.3 million people have diabetes (9.4 percent of the U.S. population)</p>
</div>
<div class="abs stat" style="left:538px;top:434px">
  <svg width="88" height="88" viewBox="0 0 88 88"><circle cx="44" cy="44" r="41" fill="none" stroke="var(--blue)" stroke-width="5"/><circle cx="44" cy="44" r="41" fill="none" stroke="var(--pink)" stroke-width="5" stroke-dasharray="40 300" transform="rotate(-90 44 44)"/><text x="44" y="47" text-anchor="middle" font-size="9" fill="#222" font-family="Roboto,Arial,sans-serif">23.1 MILLION</text></svg>
  <h3>Diagnosed</h3><p>An estimated 23.1 million people have been diagnosed with diabetes (7.2 percent of the U.S. population)</p>
</div>
<div class="abs stat" style="left:709px;top:434px">
  <svg width="88" height="88" viewBox="0 0 88 88"><circle cx="44" cy="44" r="41" fill="none" stroke="var(--pink)" stroke-width="5"/><circle cx="44" cy="44" r="41" fill="none" stroke="var(--blue)" stroke-width="5" stroke-dasharray="36 300" transform="rotate(-90 44 44)"/><text x="44" y="47" text-anchor="middle" font-size="9" fill="#222" font-family="Roboto,Arial,sans-serif">7.2 MILLION</text></svg>
  <h3>Undiagnosed</h3><p>An estimated 7.2 million adults, ages 18 years or older are undiagnosed (23.8 percent of people with diabetes)</p>
</div>

<section class="abs panel"></section>
<h2 class="abs h2" style="top:612px">Our network of healthcare providers will help you manage your diabetes.</h2>

<div class="abs card" style="left:358px;top:634px">
  <div class="icon" role="img" aria-label="Foot icon"><div></div></div>
  <h3>Pedorthist</h3><p>A professional who has specialized training in foot evaluation and modification of footwear and supportive devices such as inserts, to address conditions which affect the feet and lower limbs caused by disease, defect or injury.</p>
</div>
<div class="abs card" style="left:540px;top:634px">
  <div class="icon" role="img" aria-label="Diabetic educator icon"><div></div></div>
  <h3>Diabetic Educator</h3><p>A health professional who possesses knowledge of and experience in diabetes prevention, pre-diabetes, and diabetes management. Their main goal is to achieve individualized behavioral and treatment goals that reduce risks and optimize healthy lifestyles.</p>
</div>
<div class="abs card" style="left:721px;top:634px">
  <div class="icon" role="img" aria-label="Glucose meter icon"><div></div></div>
  <h3>Endocrinologist</h3><p>A physician who specializes in treating disorders of the endocrine system, such as diabetes.</p>
</div>
<div class="abs card" style="left:358px;top:789px">
  <div class="icon" role="img" aria-label="Food scale with apple icon"><div></div></div>
  <h3>Nutritionists</h3><p>An expert in dietetics; which includes human nutrition and the regulation of diet. A dietitian alters their patient's nutrition based upon their medical condition and individual needs.</p>
</div>
<div class="abs card" style="left:539px;top:789px">
  <div class="icon" role="img" aria-label="Feet icon"><div></div></div>
  <h3>Podiatrist</h3><p>A doctor qualified and trained to diagnose and treat conditions affecting the foot, ankle, and related structures of the leg.</p>
</div>

<h2 class="abs h2" style="top:973px">Did you know that the government has setup programs to help educate, manage,<br>and prevent your diabetes?</h2>

<div class="abs info" style="top:1008px">
  <p><b>Pedorthist Services - DIABETIC SHOES -</b> the furnishing and fitting of either one pair of custom-molded shoes and inserts or one pair of extra-depth shoes each calendar year. Federal Care Plan also covers 2 additional pairs of inserts each calendar year for custom-molded shoes and 3 pairs of inserts each calendar year for extra-depth shoes. Federal Care Plan will cover shoe modifications instead of inserts.</p>
  <p><b>Diabetic Educators - DIABETES SELF-MANAGEMENT TRAINING (DSMT) –</b> The purpose of Federal Care Plan's DSMT benefit is to give beneficiaries the knowledge and skills needed to adopt diabetes self-care behaviors and to make lifestyle changes needed to improve health outcomes. Beneficiaries are covered for a total of 10 hours of initial training within a continuous 12-month period and 2 hours of follow-up training each year after that, as needed. Courses are offered</p>
  <p><b>Nutritionists - MEDICAL NUTRITION THERAPY -</b> often abbreviated as <b>MNT</b>, is an evidence-based medical approach to treating certain chronic conditions through the use of an individually-tailored <b>NUTRITION PLAN</b>. This nutrition plan is ordered and approved by a primary care physician and implemented by a <b>REGISTERED NUTRITIONIST</b></p>
  <p><b>Podiatrist –</b> Foot exams - podiatrist services such as foot exams every 6 months, foot injuries or diseases (like hammer toes, bunion deformities, and heel spurs).</p>
</div>

<footer class="abs footer"><span>Copyright@ 2018 Glucose Guidance Circle</span><span>Privacy Policy | Terms &amp; Condition</span></footer>

<div class="abs tab" style="top:102px;height:93px"><span>Sign up - Newsletter</span></div>
<div class="abs tab" style="top:206px;height:106px"><span>Healthcare professional</span></div>
</body>
</html>
```